Brindle Children's Center - Child Care brochure

I just bought a new child care and completely renovated the space. We are also designing a new website, so I need the brochure to match that with updated info. www.brindlechildrenscenter.com - Information on there is current. We expect to have the new one up and running in the next few days. We have new photo's that I'd like to be added to the flyer too. ps. the boys in the pictures are mine, so i would appreciate one of them being added :). support@pixelhavenweb.com has details on the website (dev.brindlechildrenscenter.com). The child care program is only open during the ski season - i.e. a resort facility catering to high end clients.
I'm attaching the the website information, the flyer I created, logo files and pictures.

dev.brindlechildrenscenter.com Added Sunday, September 24, 2017

Target Market(s)

Parents of young children

Font styles to use
Other font styles liked:
• "Things we said" & "Calibri Light"

Colors
cfeae6
fef1ee

Requirements
Must have
• Pictures of children. sleek design - winter, mountain theme. Check with website designer on new website.
Nice to have
• prices included
Should not have
• Kid like artwork

```html
<!DOCTYPE html>
<html lang="en">
<head>
<meta charset="utf-8">
<title>Brindle Children's Center – Brochure</title>
<link href="https://fonts.googleapis.com/css2?family=Source+Sans+3:wght@400;600;700&display=swap" rel="stylesheet">
<style>
  :root{
    --brand-red:#e8262b;
    --brand-blue:#2e3f9c;
    --ink:#2b2b2b;
    --paper:#ffffff;
    --panel-shade:#e4e4e6;
    --dark-base:#2a2a2c;
    --dark-top:#4a4a4e;
  }
  html,body{margin:0;padding:0;width:1200px;height:906px;overflow:hidden;background:var(--paper);}
  .brochure{position:relative;width:1200px;height:906px;overflow:hidden;background:var(--paper);
    font-family:"Source Sans 3",Arial,sans-serif;color:var(--ink);}
  .top-band{position:absolute;left:0;top:0;width:1200px;height:28px;background:var(--brand-red);}
  .panel{position:absolute;top:28px;height:878px;width:400px;}
  .panel--left{left:0;background:linear-gradient(90deg,var(--paper) 82%,var(--panel-shade) 100%);}
  .panel--middle{left:400px;background:linear-gradient(90deg,var(--panel-shade) 0%,var(--paper) 14%,var(--paper) 84%,var(--panel-shade) 100%);}
  .panel--right{left:800px;background:linear-gradient(90deg,var(--panel-shade) 0%,var(--paper) 16%);}
  .swoosh{position:absolute;left:0;top:0;width:1200px;height:906px;}
  .block{position:absolute;}
  .heading{margin:0;color:var(--brand-red);font-weight:700;font-size:23px;line-height:28px;}
  .subheading{margin:0;color:var(--brand-red);font-weight:700;font-size:20px;line-height:25px;}
  .copy{margin:0;font-size:16.6px;line-height:21.4px;}
  .copy + .copy{margin-top:12px;}
  .bullets{list-style:none;margin:0;padding:0;font-size:16.6px;line-height:21.4px;}
  .bullets li{position:relative;padding-left:25px;}
  .bullets li::before{content:"";position:absolute;left:0;top:6px;width:10px;height:10px;border-radius:50%;background:var(--brand-red);}
  .bullets--spaced li + li{margin-top:12px;}
  .photo{position:absolute;}
</style>
</head>
<body>
<div class="brochure">
  <div class="panel panel--left"></div>
  <div class="panel panel--middle"></div>
  <div class="panel panel--right"></div>
  <div class="top-band"></div>

  <svg class="swoosh" viewBox="0 0 1200 906" aria-hidden="true">
    <defs>
      <linearGradient id="darkFill" x1="0" y1="0" x2="0" y2="1">
        <stop offset="0" stop-color="var(--dark-top)"/>
        <stop offset="1" stop-color="var(--dark-base)"/>
      </linearGradient>
    </defs>
    <path d="M0,850 C200,880 450,900 650,840 C800,790 1000,745 1200,760 L1200,906 L0,906 Z" fill="url(#darkFill)"/>
    <path d="M0,808 C250,838 500,858 700,818 S1000,708 1200,723 L1200,760 C1000,745 800,790 650,840 C450,900 200,880 0,850 Z" fill="var(--brand-red)"/>
    <path d="M0,800 C250,830 500,850 700,810 S1000,700 1200,715" fill="none" stroke="var(--brand-blue)" stroke-width="8"/>
  </svg>

  <!-- Left panel -->
  <section class="block" style="left:28px;top:44px;width:365px;">
    <h1 class="heading">Welcome to the Brindle Children's<br>Center!</h1>
  </section>
  <section class="block" style="left:28px;top:113px;width:340px;">
    <p class="copy">When you hit the slopes you want to make sure your child has a great day too. At the Brindle Children's Center you can be sure that your child receives the best care possible – and has a great time to boot! Located on the slopes of world famous Brindle Ski Resort, you can drop off your child at a safe, and fun center and step out the door to the slopes.</p>
  </section>
  <section class="block" style="left:28px;top:314px;width:345px;">
    <h2 class="heading">Our Services</h2>
    <p class="copy" style="margin-top:10px;">The Brindle Children's Center is a full service childcare facility that caters to children from six weeks to nine years old. Infants, toddlers, and young children can explore the activities and toys available in the Center. Children ages four and older have the option to join Brindle's legendary Rolf Anders Ski School and spend part or all of the day learning from one of Brindle's friendly instructors.</p>
  </section>
  <section class="block" style="left:28px;top:580px;width:345px;">
    <h2 class="subheading">Children visiting the center can look forward to the following activities:</h2>
    <ul class="bullets" style="margin-top:11px;">
      <li>Dramatic play</li>
      <li>Arts and Crafts</li>
      <li>Discovery Science</li>
      <li>Snow Play</li>
      <li>Games</li>
      <li>Music</li>
      <li>Nutritious lunch and snacks</li>
    </ul>
  </section>

  <!-- Middle panel -->
  <section class="block" style="left:429px;top:44px;width:345px;">
    <h2 class="heading">Our Program</h2>
    <p class="copy" style="margin-top:22px;">The Brindle Children's Center is fully accredited by the State of Utah and offers a program that caters to your child's needs:</p>
    <p class="copy" style="margin-top:21px;">Infant Care – Our infant care program is open to children over six weeks. We will tailor a program to meet your child's daily schedule. Pagers are available for nursing mothers and concerned parents.</p>
    <p class="copy">Toddlers – Children ages 18-months to three years want to explore just about everything! Creative art projects, musical games, and large muscle activities will keep your little one active and happy all day.</p>
    <p class="copy">Ages Three and Up – With their teacher and new friends, your child will explore the wonder of Brindle snow, enjoy art projects, and choose from a variety of activities that challenge the imagination.</p>
    <p class="copy">Ski School – The Brindle Children's Center works closely with the famous Rolf Anders Ski School. If you wish to have your child (ages 4 and up) participate in a group ski lesson, we will take your child to meet their ski class and pick them up after. Private lessons are also available for any age.</p>
  </section>

  <!-- Right panel -->
  <section class="block" style="left:833px;top:44px;width:340px;">
    <h2 class="heading">Our Staff</h2>
    <p class="copy" style="margin-top:22px;">At the Brindle Children's Center our staff takes pride in creating a nurturing and creative atmosphere where your child can learn and grow. Each member of our staff is continuously trained in Early Childhood Education, CPR and first aid. We work together as a team to provide the best care possible for your child.</p>
  </section>
  <section class="block" style="left:833px;top:286px;width:340px;">
    <h2 class="heading">Things to bring with you:</h2>
    <ul class="bullets bullets--spaced" style="margin-top:20px;">
      <li>For Infants, parents should supply diapers, wipes, a change of clothes, strained food (yum), and formula.</li>
      <li>For Toddlers, parents should supply diapers, wipes, and a change of clothes.</li>
      <li>For Ages 3 and Up, parents should supply a change of clothes, snow gear including: coat, hat, gloves, and snow pants, boots, and eye protection (sun glasses or goggles).</li>
    </ul>
  </section>

  <!-- Photos -->
  <svg class="photo" style="left:297px;top:705px;" width="191" height="188" viewBox="0 0 191 188" role="img" aria-label="Photo of an infant wearing a blue flower headband">
    <defs><linearGradient id="photoInfant" x1="0" y1="0" x2="1" y2="1"><stop offset="0" stop-color="#c9a98f"/><stop offset="1" stop-color="#7f8fa0"/></linearGradient></defs>
    <polygon points="55,3 136,3 188,55 188,133 136,185 55,185 3,133 3,55" fill="url(#photoInfant)" stroke="var(--brand-red)" stroke-width="5"/>
  </svg>
  <svg class="photo" style="left:531px;top:725px;" width="270" height="181" viewBox="0 0 270 181" role="img" aria-label="Photo of a toddler girl playing with a doll in the play corner">
    <defs><linearGradient id="photoToddler" x1="0" y1="0" x2="1" y2="1"><stop offset="0" stop-color="#d8cfc4"/><stop offset="1" stop-color="#8a7d74"/></linearGradient></defs>
    <polygon points="78,3 192,3 267,78 267,184 3,184 3,78" fill="url(#photoToddler)" stroke="#111" stroke-width="5"/>
  </svg>
  <svg class="photo" style="left:844px;top:585px;" width="253" height="306" viewBox="0 0 253 306" role="img" aria-label="Photo of a young girl playing with wooden toys at a table">
    <defs><linearGradient id="photoGirl" x1="0" y1="0" x2="1" y2="1"><stop offset="0" stop-color="#cdb79a"/><stop offset="1" stop-color="#8fa69a"/></linearGradient></defs>
    <polygon points="72,3 181,3 250,72 250,234 181,303 72,303 3,234 3,72" fill="url(#photoGirl)" stroke="var(--brand-red)" stroke-width="5"/>
  </svg>
</div>
</body>
</html>
```